Harbourlight Campus Lodgings needs a business card design

Hi Guys,

We are a Student Accommodation company in Australia. We already have a logo which I will submit.

I will require the design of the business cards from you.

I am after something that looks clean, modern and that people feel interested and actually want to contact us.

We would like to see designs that are innovative.

On the business cards I will require to have:

Employee Name
Position
Phone number
Email
Facebook page

I hope you can help me with this project guys as I have heard really good things from you.

```html
<!DOCTYPE html>
<html lang="en">
<head>
<meta charset="utf-8">
<title>Harbourlight Campus Lodgings – Business Card</title>
<link rel="stylesheet" href="https://fonts.googleapis.com/css2?family=Open+Sans:wght@400;600;700&family=Oswald:wght@500;700&display=swap">
<style>
  :root {
    --page: #ece8e1;
    --card-white: #ffffff;
    --yellow: #f2c12e;
    --yellow-deep: #e6ad1f;
    --green: #2fa55a;
    --green-light: #8fd04a;
    --green-mid: #3cb55b;
    --green-dark: #17914a;
    --map-green: #22a85a;
    --ink: #555a5c;
    --white: #ffffff;
  }
  * { box-sizing: border-box; margin: 0; padding: 0; }
  html, body {
    width: 1200px; height: 1023px; overflow: hidden;
    background: var(--page);
    font-family: "Open Sans", Arial, sans-serif;
  }
  .stage {
    position: relative; width: 1200px; height: 1023px;
    display: flex; align-items: center; justify-content: center; gap: 50px;
  }
  .card {
    position: relative; width: 540px; height: 310px; overflow: hidden;
    border-radius: 4px;
    box-shadow: 0 10px 28px rgba(0,0,0,.18), 0 2px 6px rgba(0,0,0,.12);
  }

  /* Front */
  .card--front { background: var(--card-white); }
  .card__bands { position: absolute; inset: 0; }
  .brand {
    position: absolute; left: 34px; top: 150px;
    display: flex; align-items: center; gap: 10px;
  }
  .brand__mark { width: 16px; height: 16px; background: var(--yellow); }
  .brand__name {
    font-weight: 700; font-size: 17px; letter-spacing: .5px;
    color: var(--green); text-transform: uppercase;
  }
  .person { position: absolute; left: 34px; top: 190px; }
  .person__name {
    font-family: "Oswald", "Arial Narrow", sans-serif; font-weight: 500;
    font-size: 20px; letter-spacing: .8px; color: var(--green-mid);
    text-transform: uppercase; line-height: 1.1;
  }
  .person__role { font-size: 13px; color: var(--ink); margin-top: 2px; }
  .contacts { list-style: none; margin-top: 12px; }
  .contacts li {
    display: flex; align-items: center; gap: 8px;
    font-size: 12.5px; color: var(--ink); line-height: 20px;
  }
  .contacts svg { width: 12px; height: 12px; flex: none; }

  /* Back */
  .card--back {
    background: linear-gradient(120deg, var(--green-dark) 0%, var(--green-mid) 45%, var(--green-light) 100%);
  }
  .back__map {
    position: absolute; left: 150px; top: 70px; width: 320px; height: 190px;
    background: var(--map-green);
    border-radius: 40% 55% 45% 60% / 50% 45% 60% 50%;
    opacity: .9;
  }
  .back__name {
    position: absolute; left: 200px; top: 115px; text-align: center;
    font-family: "Oswald", "Arial Narrow", sans-serif; color: var(--white);
    text-transform: uppercase; line-height: .95;
  }
  .back__name .line1 { font-weight: 700; font-size: 34px; letter-spacing: 1px; display: block; }
  .back__name .line2 { font-weight: 500; font-size: 14px; letter-spacing: 6px; display: block; margin-top: 6px; }
  .back__tagline {
    position: absolute; left: 0; right: 0; bottom: 16px; text-align: center;
    font-size: 11.5px; color: var(--white); letter-spacing: .3px;
  }
</style>
</head>
<body>
<main class="stage">

  <section class="card card--front" aria-label="Business card front">
    <svg class="card__bands" viewBox="0 0 540 310" aria-hidden="true">
      <polygon points="300,0 540,0 540,130 360,100" fill="var(--yellow)"/>
      <polygon points="330,95 540,120 540,170 300,140" fill="var(--yellow-deep)" opacity=".85"/>
    </svg>

    <div class="brand">
      <span class="brand__mark"></span>
      <span class="brand__name">Harbourlight Campus Lodgings</span>
    </div>

    <div class="person">
      <p class="person__name">Maren Colquhoun</p>
      <p class="person__role">Creative Director</p>
      <ul class="contacts">
        <li>
          <svg viewBox="0 0 12 12"><rect width="12" height="12" rx="2" fill="var(--green)"/><path d="M4 3h1.3l.6 1.6-.8.6a4 4 0 0 0 1.9 1.9l.6-.8 1.6.6V8.2A.8.8 0 0 1 8.4 9 5.4 5.4 0 0 1 3 3.6.8.8 0 0 1 4 3z" fill="#fff"/></svg>
          0400 123 987
        </li>
        <li>
          <svg viewBox="0 0 12 12"><rect width="12" height="12" rx="2" fill="var(--green)"/><rect x="2.5" y="3.5" width="7" height="5" fill="none" stroke="#fff" stroke-width=".9"/><path d="M2.5 3.5 6 6.3l3.5-2.8" fill="none" stroke="#fff" stroke-width=".9"/></svg>
          maren@harbourlight.com.au
        </li>
        <li>
          <svg viewBox="0 0 12 12"><rect width="12" height="12" rx="2" fill="var(--green)"/></svg>
          HarbourlightLodgings
        </li>
      </ul>
    </div>
  </section>

  <section class="card card--back" aria-label="Business card back">
    <svg class="card__bands" viewBox="0 0 540 310" aria-hidden="true">
      <polygon points="0,0 330,0 260,120 0,150" fill="var(--green-dark)" opacity=".55"/>
    </svg>
    <div class="back__map" role="img" aria-label="Map of Australia"></div>
    <p class="back__name">
      <span class="line1">Harbourlight</span>
      <span class="line2">Campus Lodgings</span>
    </p>
    <p class="back__tagline">Professional Management of Student Accommodation in Australia</p>
  </section>

</main>
</body>
</html>
```